Scoopa Verde label for 16oz jar

We need a design for a label for a 16oz glass jar for salsa (dimensions in inches- 2.75 x9.5). Name of salsa is “Scoopa Verde” and needs to include a place for medium or hot for the different flavors. Looking for bright Fiesta colors but a mature look. Attached is an image of the coloring scheme we like. There will need to be nutrition facts on one end and a description of the product/flavor on the other side of the label. Ultimately at this point looking for brand design.

```html
<!DOCTYPE html>
<html lang="en">
<head>
<meta charset="utf-8">
<title>Scoopa Verde – Jar Label</title>
<link rel="stylesheet" href="https://fonts.googleapis.com/css2?family=Abril+Fatface&family=Poppins:wght@400;500;600&family=Libre+Franklin:wght@400;600;800;900&display=swap">
<style>
  :root {
    --pink: #e0479a;
    --yellow: #fbbd16;
    --blue-dark: #1a5ea8;
    --blue-light: #27a3dc;
    --navy: #17509e;
    --red: #e3141e;
    --green: #8cc63f;
    --white: #ffffff;
    --ink: #111111;
    --page: #f2f2f2;
    --energy: #e3141e;
    --fat: #f5a200;
    --satfat: #f5a200;
    --sugar: #2fb37a;
    --salt: #1fb7a6;
  }
  * { box-sizing: border-box; margin: 0; padding: 0; }
  html, body { width: 1200px; height: 860px; overflow: hidden; background: var(--page); }
  .canvas { position: relative; width: 1200px; height: 860px; }

  .label {
    position: absolute; left: 30px; top: 255px;
    width: 1305px; height: 400px;
    transform: scale(0.8736); transform-origin: top left;
    background: var(--pink); overflow: hidden;
    box-shadow: 0 6px 14px rgba(0,0,0,.25);
  }
  .label__shapes { position: absolute; inset: 0; }

  .description {
    position: absolute; left: 40px; width: 360px; text-align: center;
    font-family: "Poppins", sans-serif; color: var(--white);
    font-size: 15px; line-height: 19.3px;
  }
  .description--top { top: 35px; }
  .description--bottom { top: 298px; }

  .nutri-badges { position: absolute; left: 58px; top: 198px; display: flex; gap: 14px; }
  .badge {
    width: 54px; height: 74px; background: var(--white);
    border: 1.5px solid var(--white); border-radius: 12px 12px 18px 18px;
    outline: 1px solid rgba(255,255,255,.6);
    display: flex; flex-direction: column; align-items: center; overflow: hidden;
    font-family: "Poppins", sans-serif; color: var(--white);
    background: transparent; box-shadow: inset 0 0 0 1.5px var(--white);
  }
  .badge__name { font-size: 12px; font-weight: 500; margin-top: 10px; line-height: 1.1; text-align: center; }
  .badge__name--small { font-size: 10px; margin-top: 6px; }
  .badge__value { font-size: 12px; font-weight: 500; }
  .badge__pct {
    margin-top: auto; width: 100%; height: 24px; border-radius: 0 0 16px 16px;
    font-size: 13px; font-weight: 600; text-align: center; line-height: 24px;
  }
  .badge__pct--energy { background: var(--energy); }
  .badge__pct--fat { background: var(--fat); }
  .badge__pct--satfat { background: var(--satfat); }
  .badge__pct--sugar { background: var(--sugar); }
  .badge__pct--salt { background: var(--salt); }

  .brand-panel {
    position: absolute; left: 433px; top: 70px; width: 437px; height: 260px;
    background: var(--white);
  }
  .brand-panel__frame {
    position: absolute; left: 10px; top: 12px; right: 10px; bottom: 8px;
    border: 5px solid var(--green);
  }
  .brand-name {
    position: absolute; left: 0; right: 0; top: 36px; text-align: center;
    font-family: "Abril Fatface", serif; color: var(--navy);
    font-size: 66px; line-height: 70px; letter-spacing: 1px;
  }
  .flavor-tag {
    position: absolute; left: 65px; bottom: 0; width: 307px; height: 58px;
    background: var(--red); border-radius: 60px 60px 0 0;
    font-family: "Abril Fatface", serif; color: var(--white);
    font-size: 31px; text-align: center; line-height: 58px; letter-spacing: .5px;
  }
  .tagline {
    position: absolute; left: 433px; width: 437px; top: 335px; text-align: center;
    font-family: "Abril Fatface", serif; color: var(--white);
    font-size: 18px; line-height: 22px; letter-spacing: .3px;
  }

  .nutrition-facts {
    position: absolute; left: 928px; top: 48px; width: 334px; height: 304px;
    background: var(--white); border: 2px solid var(--ink); padding: 4px 6px;
    font-family: "Libre Franklin", sans-serif; color: var(--ink); font-size: 9px;
  }
  .nf__title { font-weight: 900; font-size: 36px; line-height: 38px; letter-spacing: -.5px; border-bottom: 1px solid var(--ink); }
  .nf__row { display: flex; justify-content: space-between; line-height: 14px; border-bottom: .5px solid #555; }
  .nf__row b { font-weight: 800; }
  .nf__servings { font-size: 10px; line-height: 12px; margin-top: 3px; }
  .nf__size { font-size: 11.5px; font-weight: 800; border-bottom: 7px solid var(--ink); line-height: 15px; }
  .nf__amount { font-size: 6.5px; font-weight: 800; margin-top: 3px; }
  .nf__calories { display: flex; justify-content: space-between; font-weight: 900; font-size: 21px; line-height: 22px; border-bottom: 4px solid var(--ink); }
  .nf__dv { text-align: right; font-size: 7px; font-weight: 600; line-height: 12px; border-bottom: .5px solid #555; }
  .nf__indent { padding-left: 12px; }
  .nf__indent2 { padding-left: 22px; }
  .nf__protein { border-bottom: 7px solid var(--ink); }
  .nf__foot { font-size: 6.5px; line-height: 8px; margin-top: 5px; }
</style>
</head>
<body>
<main class="canvas">
  <section class="label" aria-label="Scoopa Verde jar label">
    <svg class="label__shapes" viewBox="0 0 1305 400" width="1305" height="400" aria-hidden="true">
      <path fill="var(--yellow)" d="M708,0 L1305,0 L1305,400 L700,400 C690,300 690,150 710,80 C720,40 712,15 708,0 Z"/>
      <path fill="var(--blue-dark)" d="M735,400 L735,290 C770,220 850,160 930,175 L1305,215 L1305,400 Z"/>
      <path fill="var(--blue-light)" d="M0,400 L0,350 C110,330 290,262 420,288 C480,300 520,325 570,330 L735,330 L745,400 Z"/>
    </svg>

    <p class="description description--top">Lorem ipsum dolor sit amet, consectetuer adipiscing elit, sed diam nonummy nibh euismod tincidunt ut laoreet dolore magna aliquam erat volutpat. Ut wisi enim ad minim veniam, quis nostrud exerci tation ullamcorper suscipit lobortis nisl ut aliquip ex ea commodo consequat. Duis autem vel eum iriure dolor in</p>

    <div class="nutri-badges">
      <div class="badge"><span class="badge__name">Energy</span><span class="badge__value">245kcal</span><span class="badge__pct badge__pct--energy">12%</span></div>
      <div class="badge"><span class="badge__name">Fat</span><span class="badge__value">12g</span><span class="badge__pct badge__pct--fat">14%</span></div>
      <div class="badge"><span class="badge__name badge__name--small">Satura-<br>ted Fat</span><span class="badge__value">2g</span><span class="badge__pct badge__pct--satfat">10%</span></div>
      <div class="badge"><span class="badge__name">Sugars</span><span class="badge__value">4g</span><span class="badge__pct badge__pct--sugar">8%</span></div>
      <div class="badge"><span class="badge__name">Salt</span><span class="badge__value">0.2g</span><span class="badge__pct badge__pct--salt">9%</span></div>
    </div>

    <p class="description description--bottom">Lorem ipsum dolor sit amet, consectetuer adipiscing elit, sed diam nonummy nibh euismod tincidunt ut laoreet dolore magna</p>

    <div class="brand-panel">
      <div class="brand-panel__frame"></div>
      <h1 class="brand-name">Scoopa<br>Verde</h1>
      <div class="flavor-tag">Red Sauce</div>
    </div>
    <p class="tagline">for natural and genuie<br>products branding</p>

    <div class="nutrition-facts">
      <h2 class="nf__title">Nutrition Facts</h2>
      <p class="nf__servings">4 servings per container/6 raciones por envase</p>
      <div class="nf__size" style="display:flex;justify-content:space-between"><span>Serving size</span><span>1 cup/1 taza (180g)</span></div>
      <p class="nf__amount">Amount per serving</p>
      <div class="nf__calories"><span>Calories</span><span>245</span></div>
      <p class="nf__dv">% Daily Value*/% Valor diario*</p>
      <div class="nf__row"><span><b>Total Fat/Grasa total</b> 12g</span><b>14%</b></div>
      <div class="nf__row nf__indent"><span>Saturated Fat/Grasa Saturada 2g</span><b>10%</b></div>
      <div class="nf__row nf__indent"><span><i>Trans</i> Fat/Grasa <i>Trans</i> 0g</span><span></span></div>
      <div class="nf__row"><span><b>Cholesterol/Colesterol</b> 8mg</span><b>3%</b></div>
      <div class="nf__row"><span><b>Sodium/Sodio</b> 210mg</span><b>9%</b></div>
      <div class="nf__row"><span><b>Total Carbohydrate/Carbohidrato Total</b> 34g</span><b>12%</b></div>
      <div class="nf__row nf__indent"><span>Dietary Fiber/Fibra Dietética 7g</span><b>25%</b></div>
      <div class="nf__row nf__indent"><span>Total Sugars/Azúcares Totales 5g</span><span></span></div>
      <div class="nf__row nf__indent2"><span>Includes 4g Added Sugars/Incluye 4 g de azúcares añadidos</span><b>8%</b></div>
      <div class="nf__row nf__protein"><span><b>Protein/Proteínas</b> 11g</span><span></span></div>
      <p class="nf__foot">* The % Daily Value (DV) tells you how much a nutrient in a serving of food contributes to a daily diet. 2,000 calories a day is used for general nutrition advice.</p>
    </div>
  </section>
</main>
</body>
</html>
```